Project Finance Brochure

We are a finance fund helping bring energy efficiency and clean energy projects into the world. We would like a professionally created back and front brochure. Please take our internally created piece and work your magic!

Target Market(s)

We are targeting building owners, hotel operators, manufacturing plant engineers.

Industry/Entity Type

Finance

Font styles to use
Sans Serif

Requirements
Must have
• Must be clear and easy to understand. Flow charts help.
Nice to have
• Colors, fonts.

```html
<!DOCTYPE html>
<html lang="en">
<head>
<meta charset="utf-8">
<title>Verdantis Capital – Brochure</title>
<link href="https://fonts.googleapis.com/css2?family=Montserrat:wght@300;400;600;700&display=swap" rel="stylesheet">
<style>
  :root {
    --bg: #e4e4e4;
    --slate: #58595b;
    --slate-dark: #48494b;
    --green: #7cc242;
    --white: #ffffff;
    --ink: #6d6e70;
    --photo-green-light: #8fb3a0;
    --photo-green-dark: #2e3e36;
    --photo-grey-light: #b9bbbc;
    --photo-grey-dark: #4b4d4f;
  }
  * { margin: 0; padding: 0; box-sizing: border-box; }
  html, body { width: 1200px; height: 1000px; overflow: hidden; }
  body {
    background: var(--bg);
    font-family: "Montserrat", sans-serif;
    position: relative;
  }
  .panel {
    position: absolute;
    top: 50px;
    width: 420px;
    height: 900px;
    overflow: hidden;
    box-shadow: 0 6px 18px rgba(0,0,0,0.18);
  }
  .panel svg.art { position: absolute; inset: 0; }
  .back-panel { left: 160px; background: var(--slate); }
  .front-cover { left: 620px; background: var(--photo-green-dark); }

  /* back panel text */
  .back-contact {
    position: absolute;
    left: 40px;
    top: 300px;
    color: var(--white);
  }
  .wordmark {
    font-family: "Montserrat", sans-serif;
    font-weight: 400;
    letter-spacing: -0.5px;
    white-space: nowrap;
  }
  .back-contact .wordmark { font-size: 26px; color: var(--white); }
  .contact-list { list-style: none; margin-top: 30px; font-size: 10px; font-weight: 300; line-height: 1.45; }
  .contact-list li { display: flex; align-items: flex-start; gap: 7px; margin-bottom: 4px; }
  .contact-list svg { flex: none; margin-top: 1px; }
  .back-web { margin-top: 22px; font-size: 13px; font-weight: 300; letter-spacing: 0.3px; }
  .back-web strong { font-weight: 700; }

  /* front cover text */
  .cover-title {
    position: absolute;
    left: 30px;
    top: 520px;
    transform-origin: left top;
    transform: rotate(-12.1deg);
  }
  .cover-title .wordmark { font-size: 44px; color: var(--green); line-height: 1; }
  .cover-tagline {
    position: absolute;
    left: 24px;
    top: 621px;
    transform-origin: left top;
    transform: rotate(-12.1deg);
    color: var(--white);
    font-size: 14px;
    font-weight: 300;
    letter-spacing: 0.6px;
    white-space: nowrap;
  }
  .cover-tagline strong { font-weight: 700; }
  .cover-web {
    position: absolute;
    left: 222px;
    top: 720px;
    transform-origin: left top;
    transform: rotate(-12.1deg);
    color: var(--white);
    font-size: 15px;
    font-weight: 300;
    white-space: nowrap;
  }
  .cover-web strong { font-weight: 700; }
</style>
</head>
<body>

  <!-- Back panel -->
  <section class="panel back-panel">
    <svg class="art" width="420" height="900" viewBox="0 0 420 900">
      <defs>
        <linearGradient id="buildingTone" x1="0" y1="0" x2="1" y2="1">
          <stop offset="0" stop-color="var(--photo-grey-light)"/>
          <stop offset="1" stop-color="var(--photo-grey-dark)"/>
        </linearGradient>
      </defs>
      <polygon points="330,0 420,0 420,900 200,900" fill="url(#buildingTone)"
               role="img" aria-label="Photo of a modern office building with exposed steel pipework and windows"/>
      <polygon points="322,0 334,0 306,230 294,230" fill="var(--green)"/>
      <polygon points="218,770 244,770 214,840" fill="var(--green)"/>
    </svg>
    <div class="back-contact">
      <div class="wordmark">Verdantis Capital</div>
      <ul class="contact-list">
        <li>
          <svg width="9" height="12" viewBox="0 0 9 12"><path d="M4.5 0C2 0 0 2 0 4.4 0 7.6 4.5 12 4.5 12S9 7.6 9 4.4C9 2 7 0 4.5 0zm0 6.2a1.8 1.8 0 1 1 0-3.6 1.8 1.8 0 0 1 0 3.6z" fill="#fff"/></svg>
          <span>410 Harbor Crest Avenue Suite 12<br>Brookfield, CA, 94011</span>
        </li>
        <li>
          <svg width="11" height="11" viewBox="0 0 11 11"><circle cx="5.5" cy="5.5" r="5" fill="none" stroke="#fff" stroke-width="0.9"/><path d="M3.6 3.1l1 1-.5.6c.3.7.9 1.3 1.6 1.6l.6-.5 1 1-.7.8c-1.8-.3-3.4-1.9-3.7-3.7z" fill="#fff"/></svg>
          <span>555-214-7780</span>
        </li>
      </ul>
      <div class="back-web">www.<strong>verdantiscap</strong>.com</div>
    </div>
  </section>

  <!-- Front cover -->
  <section class="panel front-cover">
    <svg class="art" width="420" height="900" viewBox="0 0 420 900">
      <defs>
        <linearGradient id="plantTone" x1="0" y1="0" x2="1" y2="1">
          <stop offset="0" stop-color="var(--photo-green-light)"/>
          <stop offset="0.55" stop-color="#5d7b6c"/>
          <stop offset="1" stop-color="var(--photo-green-dark)"/>
        </linearGradient>
      </defs>
      <rect width="420" height="900" fill="url(#plantTone)"
            role="img" aria-label="Green-tinted photo of industrial steel pipes and cylindrical towers"/>
      <polygon points="300,456 420,400 420,430" fill="var(--green)"/>
      <polygon points="0,520 420,430 420,520 0,610" fill="var(--white)"/>
      <polygon points="0,610 420,520 420,560 0,650" fill="var(--slate)"/>
    </svg>
    <div class="cover-title">
      <div class="wordmark">Verdantis Capital</div>
    </div>
    <div class="cover-tagline">CLEAN ENERGY <strong>ACCELERATION PROGRAM</strong></div>
    <div class="cover-web">www.<strong>verdantiscap</strong>.com</div>
  </section>

</body>
</html>
```